KL MOTORS BANNER/SIGN DESIGN

Design a banner sign for outdoor use for KL MOTORS - a premium pre owned vehicle sales center. The size must be 36 feet in width
and 3 feet in height.

Information required: logo (attached)
-PREMIUM PRE-OWEND VEHICLE SALES
- 517.264.3081

perhaps in smaller font: BUY-SELL-TRADE

prefer white background but could possibly do red matching the logo

```html
<!DOCTYPE html>
<html lang="en">
<head>
<meta charset="utf-8">
<title>KL Motors – Outdoor Banner</title>
<link rel="stylesheet" href="https://fonts.googleapis.com/css2?family=Archivo+Black&family=Oswald:wght@600;700&display=swap">
<style>
  :root {
    --brand-red: #d90b1c;
    --ink: #111111;
    --paper: #ffffff;
    --frame: #8a8a8a;
  }
  html, body {
    margin: 0;
    padding: 0;
    width: 1200px;
    height: 900px;
    overflow: hidden;
    background: var(--paper);
  }
  .canvas {
    position: relative;
    width: 1200px;
    height: 900px;
  }
  .banner {
    position: absolute;
    left: 67px;
    top: 405px;
    width: 1067px;
    height: 89px;
    display: block;
  }
  .banner-frame { fill: var(--paper); stroke: var(--frame); stroke-width: 1; }
  .brand-circle { fill: none; stroke: var(--brand-red); stroke-width: 5; }
  .brand-divider { stroke: var(--ink); stroke-width: 2; }
  .brand-name {
    font-family: "Archivo Black", sans-serif;
    font-size: 30px;
    fill: var(--ink);
  }
  .arrow-body { fill: var(--brand-red); }
  .arrow-stripe { fill: none; stroke: var(--brand-red); stroke-width: 5; }
  .tagline {
    font-family: "Oswald", sans-serif;
    font-weight: 700;
    font-size: 31px;
    fill: var(--paper);
  }
  .phone-shadow {
    font-family: "Archivo Black", sans-serif;
    font-size: 52px;
    fill: var(--ink);
  }
  .phone {
    font-family: "Archivo Black", sans-serif;
    font-size: 52px;
    fill: var(--paper);
  }
  .service {
    font-family: "Oswald", sans-serif;
    font-weight: 600;
    font-size: 18px;
    fill: var(--ink);
  }
</style>
</head>
<body>
<div class="canvas">
  <svg class="banner" viewBox="0 0 1067 89" xmlns="http://www.w3.org/2000/svg" aria-label="KL Motors banner">
    <rect class="banner-frame" x="0.5" y="0.5" width="1066" height="88"/>

    <!-- brand -->
    <circle class="brand-circle" cx="49" cy="44.5" r="30"/>
    <line class="brand-divider" x1="95" y1="20" x2="95" y2="76"/>
    <text class="brand-name" x="108" y="58" textLength="204" lengthAdjust="spacingAndGlyphs">KL MOTORS</text>

    <!-- red arrow band -->
    <polyline class="arrow-stripe" points="318,0 348,44.5 318,89"/>
    <polyline class="arrow-stripe" points="332,0 362,44.5 332,89"/>
    <polygon class="arrow-body" points="348,0 965,0 996,44.5 965,89 348,89 378,44.5"/>

    <text class="tagline" x="667" y="34" text-anchor="middle" textLength="501" lengthAdjust="spacingAndGlyphs">PREMIUM PRE-OWNED VEHICLE SALES</text>
    <text class="phone-shadow" x="670" y="82" text-anchor="middle" textLength="506" lengthAdjust="spacingAndGlyphs">517.264.3081</text>
    <text class="phone" x="667" y="79" text-anchor="middle" textLength="506" lengthAdjust="spacingAndGlyphs">517.264.3081</text>

    <!-- services -->
    <text class="service" x="1051" y="29" text-anchor="end">• BUY</text>
    <text class="service" x="1051" y="52" text-anchor="end">• SELL</text>
    <text class="service" x="1051" y="75" text-anchor="end">• TRADE</text>
  </svg>
</div>
</body>
</html>
```